Colorful Drive Through Car Wash Website

Design of an interactive car wash website. We're going with lively colors and a fun website. Purple and and pink colors come to mind.

The website should be a good balance between professional and fun.

Target Market(s)

Drivers that need a quick drive through car wash

Number of Pages Required

1 page

Font styles to use
Sans Serif

Colors
e34297
886aae

Requirements
Must have
• Bubbles in the design.

```html
<!DOCTYPE html>
<html lang="en">
<head>
<meta charset="utf-8">
<title>Foam Harbor — Car Wash</title>
<link rel="stylesheet" href="https://fonts.googleapis.com/css2?family=Lato:wght@400;700;900&family=Open+Sans:wght@400;600;700&display=swap">
<style>
:root{
  --pink:#e34297;
  --purple:#886aae;
  --purple-deep:#7a58a8;
  --ink:#222222;
  --text:#666666;
  --muted:#888888;
  --white:#ffffff;
  --footer:#1d1d1f;
  --line:#e5e5e5;
}
*{box-sizing:border-box;margin:0;padding:0}
html,body{width:1200px;height:3015px;overflow:hidden}
body{position:relative;background:var(--white);font-family:"Open Sans",Arial,sans-serif;color:var(--text)}
.abs{position:absolute}

/* Hero */
.hero{position:absolute;left:0;top:0;width:1200px;height:630px;overflow:hidden}
.hero-photo{position:absolute;inset:0;background:linear-gradient(160deg,#8a7aa0 0%,#b79ac4 35%,#c9a6cf 55%,#9c7fae 80%,#6d5a82 100%)}
.hero-wave{position:absolute;left:0;top:530px}
.logo{position:absolute;display:flex;align-items:center;gap:12px;font-family:"Lato",sans-serif;font-weight:900;color:var(--white)}
.logo-dot{width:34px;height:34px;border-radius:50%;background:var(--white)}
.hero .logo{left:100px;top:52px;font-size:30px}
.phone-top{left:830px;top:20px;display:flex;align-items:center;gap:12px;color:var(--white);font-family:"Lato",sans-serif;font-weight:700;font-size:20px}
.phone-top .ring{width:32px;height:32px;border-radius:50%;border:2px solid var(--pink);display:flex;align-items:center;justify-content:center}
.nav{left:500px;top:74px;display:flex;gap:44px;font-family:"Lato",sans-serif;font-weight:700;font-size:16px;color:var(--white);align-items:center}
.nav .active{color:var(--pink)}
.hero-title{left:0;width:1200px;top:165px;text-align:center;font-family:"Lato",sans-serif;font-weight:900;font-size:72px;color:var(--white);letter-spacing:1px}
.hero-sub{left:0;width:1200px;top:254px;text-align:center;font-family:"Open Sans",sans-serif;font-weight:600;font-size:30px;color:var(--white)}
.hero-find{left:0;width:1200px;top:312px;text-align:center;font-weight:600;font-size:22px;color:var(--white)}
.search{left:346px;top:362px;width:504px;height:52px;display:flex}
.search-field{flex:1;background:var(--white);display:flex;align-items:center;gap:8px;padding-left:14px;font-size:15px;color:#555}
.search-go{width:62px;background:var(--pink);color:var(--white);font-family:"Lato",sans-serif;font-weight:900;font-size:18px;display:flex;align-items:center;justify-content:center}
.dots{left:562px;top:522px;display:flex;gap:6px}
.dots span{width:14px;height:14px;border-radius:50%;border:2px solid var(--white)}
.dots span.on{background:var(--white)}

/* Welcome */
.section-title{left:0;width:1200px;text-align:center;font-family:"Lato",sans-serif;font-weight:900;font-size:34px;color:var(--ink)}
.welcome-intro{left:195px;width:810px;top:742px;text-align:center;font-size:14px;line-height:26px;color:var(--muted)}
.feature{position:absolute;top:836px;width:240px;text-align:center}
.feature-ring{margin:0 auto;width:170px;height:170px;border-radius:50%;border:1px solid var(--purple);display:flex;align-items:center;justify-content:center}
.feature-ring-inner{width:152px;height:152px;border-radius:50%;border:6px solid var(--purple);display:flex;align-items:center;justify-content:center}
.feature h3{margin-top:26px;font-family:"Lato",sans-serif;font-weight:700;font-size:20px;color:var(--ink)}
.feature p{margin-top:12px;font-size:14px;line-height:24px;color:var(--muted)}

/* Booking band */
.book{left:0;top:1212px;width:1200px;height:300px}
.book-photo{position:absolute;inset:0;background:linear-gradient(180deg,#7c7c7c 0%,#a9a9a9 40%,#8e8e8e 70%,#5a5a5a 100%)}
.book-title{left:0;width:1200px;top:1292px;text-align:center;font-family:"Lato",sans-serif;font-weight:900;font-size:42px;color:var(--white)}
.btn-outline{display:flex;align-items:center;justify-content:center;border:2px solid var(--white);border-radius:28px;color:var(--white);font-family:"Lato",sans-serif;font-weight:700;font-size:16px}
.book .btn-outline{position:absolute;left:500px;top:165px;width:196px;height:54px}

/* Colorful band */
.colorful{left:0;top:1512px;width:1200px;height:432px;background:var(--purple)}
.colorful h2{position:absolute;left:98px;top:60px;font-family:"Lato",sans-serif;font-weight:900;font-size:35px;line-height:46px;color:var(--white)}
.colorful p{position:absolute;left:98px;top:166px;width:530px;font-size:14px;line-height:26px;color:var(--white)}
.colorful .btn-outline{position:absolute;left:98px;top:326px;width:140px;height:46px;font-size:14px}
.photo-circle{position:absolute;border-radius:50%;border:5px solid var(--white)}
.photo-circle.large{left:656px;top:64px;width:342px;height:342px;background:linear-gradient(90deg,#2f7ad8 0%,#2db84a 25%,#f1d423 45%,#f39323 62%,#e8322a 80%,#6a6a6a 100%)}
.photo-circle.small{left:952px;top:52px;width:176px;height:176px;background:radial-gradient(circle at 45% 50%,#e9df9a 0%,#8fa96a 55%,#44603a 100%)}

/* Blog */
.post{position:absolute;top:2096px;width:324px}
.post-photo{position:relative;width:324px;height:210px;border:2px solid #dcdcdc}
.post-photo .fill{position:absolute;inset:4px}
.post-date{position:absolute;left:-8px;bottom:18px;width:42px;height:52px;background:var(--pink);color:var(--white);text-align:center;font-family:"Lato",sans-serif}
.post-date b{display:block;font-size:22px;line-height:30px}
.post-date span{font-size:12px}
.post h3{margin-top:26px;font-family:"Lato",sans-serif;font-weight:700;font-size:19px;color:var(--ink)}
.post p{margin-top:10px;font-size:12px;line-height:22px;color:var(--muted)}
.post-meta{margin-top:14px;padding-top:12px;border-top:1px solid var(--line);display:flex;gap:22px;font-size:12px;color:var(--muted)}
.post-meta span{display:flex;align-items:center;gap:6px}

/* Footer */
.footer{left:0;top:2548px;width:1200px;height:467px}
.footer-body{position:absolute;left:0;top:70px;width:1200px;height:397px;background:var(--footer)}
.footer .logo{left:100px;top:228px;font-size:30px}
.foot-col{position:absolute;top:162px;color:var(--white)}
.foot-col h4{font-family:"Lato",sans-serif;font-weight:700;font-size:17px;margin-bottom:22px}
.foot-links li{list-style:none;font-size:12px;line-height:27px}
.foot-col p{font-size:12px;line-height:20px}
.news-field{margin-top:18px;width:254px;height:36px;background:var(--white);font-size:12px;color:#777;display:flex;align-items:center;padding-left:14px}
.news-btn{margin-top:20px;width:100px;height:34px;border-radius:18px;background:var(--pink);font-family:"Lato",sans-serif;font-weight:700;font-size:12px;display:flex;align-items:center;justify-content:center}
.contact-row{display:flex;gap:22px;font-size:12px;line-height:20px;margin-bottom:24px;align-items:flex-start}
.contact-row svg{flex:none;margin-top:2px}
.foot-rule{position:absolute;left:98px;top:372px;width:1004px;height:1px;background:#444}
.copyright{position:absolute;left:98px;top:400px;font-size:12px;color:var(--white)}
.socials{position:absolute;left:940px;top:390px;display:flex;gap:8px}
.socials span{width:26px;height:26px;border-radius:50%;border:2px solid var(--white)}
</style>
</head>
<body>

<header class="hero">
  <div class="hero-photo" role="img" aria-label="Photo of a car inside a car wash under purple-tinted light"></div>
  <div class="logo"><span class="logo-dot"></span>Foam Harbor</div>
  <div class="abs phone-top">
    <span class="ring"><svg width="14" height="14" viewBox="0 0 24 24"><path fill="#e34297" d="M6.6 10.8a15 15 0 0 0 6.6 6.6l2.2-2.2c.3-.3.7-.4 1-.2 1.1.4 2.3.6 3.6.6.6 0 1 .4 1 1V20c0 .6-.4 1-1 1A17 17 0 0 1 3 4c0-.6.4-1 1-1h3.5c.6 0 1 .4 1 1 0 1.3.2 2.5.6 3.6.1.3 0 .7-.2 1z"/></svg></span>
    Call us on : 1 800 555 0142
  </div>
  <nav class="abs nav">
    <span class="active">HOME</span><span>ABOUT</span><span>SERVICES</span><span>LOCATION</span><span>CONTACT US</span>
    <svg width="16" height="16" viewBox="0 0 24 24"><circle cx="10" cy="10" r="7" fill="none" stroke="#fff" stroke-width="3"/><path d="M15 15l6 6" stroke="#fff" stroke-width="3"/></svg>
  </nav>
  <h1 class="abs hero-title">FOAM HARBOR</h1>
  <div class="abs hero-sub">We are a Car Wash Company</div>
  <div class="abs hero-find">Find your Local Car wash</div>
  <div class="abs search">
    <div class="search-field"><svg width="10" height="14" viewBox="0 0 10 14"><path d="M5 0a5 5 0 0 0-5 5c0 4 5 9 5 9s5-5 5-9a5 5 0 0 0-5-5zm0 7a2 2 0 1 1 0-4 2 2 0 0 1 0 4z" fill="#555"/></svg>Enter Zipcode</div>
    <div class="search-go">GO</div>
  </div>
  <div class="abs dots"><span class="on"></span><span></span><span></span><span></span></div>
  <svg class="hero-wave" width="1200" height="100" viewBox="0 0 1200 100">
    <path fill="#fff" d="M0,100 L0,60 C40,20 100,20 140,55 C170,10 260,5 300,50 C340,25 400,25 440,60 C490,0 600,0 650,55 C690,25 750,25 790,60 C840,10 930,10 970,50 C1010,20 1080,20 1120,55 C1150,35 1190,35 1200,45 L1200,100 Z"/>
    <path fill="none" stroke="#7a58a8" stroke-width="7" d="M0,60 C40,20 100,20 140,55 C170,10 260,5 300,50 C340,25 400,25 440,60 C490,0 600,0 650,55 C690,25 750,25 790,60 C840,10 930,10 970,50 C1010,20 1080,20 1120,55 C1150,35 1190,35 1200,45"/>
  </svg>
</header>

<section class="welcome">
  <h2 class="abs section-title" style="top:680px">WELCOME TO FOAM HARBOR</h2>
  <p class="abs welcome-intro">Nam libero tempore, cum soluta nobis est eligendi optio cumque nihil impedit quo minus id quod maxime placeat facere possimus, omnis voluptas assumenda est, omnis dolor repellen poribus autem quibusdam</p>

  <div class="feature" style="left:86px">
    <div class="feature-ring"><div class="feature-ring-inner">
      <svg width="60" height="60" viewBox="0 0 24 24"><path fill="#e34297" d="M2 10h4v11H2zM8 21V10l5-8c1.5 0 2.5 1 2.2 2.6L14.5 8H20c1.2 0 2 1 1.8 2.2l-1.6 8.8c-.2 1.2-1.1 2-2.3 2z"/></svg>
    </div></div>
    <h3>High-Quality</h3>
    <p>Omnis dolor repellendu emp oribus autem quibusdam et aut officiis aut recessiru</p>
  </div>
  <div class="feature" style="left:348px">
    <div class="feature-ring"><div class="feature-ring-inner">
      <svg width="60" height="60" viewBox="0 0 24 24"><path fill="#e34297" d="M2 3v8l11 11 9-9L11 2H3zm5 2.5a1.5 1.5 0 1 1 0 3 1.5 1.5 0 0 1 0-3z"/></svg>
    </div></div>
    <h3>Affordable Prices</h3>
    <p>Omnis dolor repellendu emp oribus autem quibusdam et aut officiis aut recessiru</p>
  </div>
  <div class="feature" style="left:610px">
    <div class="feature-ring"><div class="feature-ring-inner">
      <svg width="56" height="56" viewBox="0 0 24 24"><path fill="#e34297" d="M12 1l2.4 3.1 3.9-.6.6 3.9L22 9.6l-2 3.4 1.4 3.7-3.8 1.2-1.1 3.8-3.5-1.6L9.5 21.7 8 18 4.2 17l.8-3.9L2.3 10l3.2-2.3L5.6 3.8l3.9.3z"/></svg>
    </div></div>
    <h3>Best Experience</h3>
    <p>Omnis dolor repellendu emp oribus autem quibusdam et aut officiis aut recessiru</p>
  </div>
  <div class="feature" style="left:872px">
    <div class="feature-ring"><div class="feature-ring-inner">
      <svg width="58" height="58" viewBox="0 0 24 24"><circle cx="12" cy="12" r="9.5" fill="none" stroke="#e34297" stroke-width="3"/><path d="M12 6.5V12h4.5" fill="none" stroke="#e34297" stroke-width="2.8" stroke-linecap="round"/></svg>
    </div></div>
    <h3>On Time service</h3>
    <p>Omnis dolor repellendu emp oribus autem quibusdam et aut officiis aut recessiru</p>
  </div>
</section>

<section class="abs book">
  <div class="book-photo" role="img" aria-label="Black and white photo of a foam-covered car between car wash brushes"></div>
  <div class="btn-outline">BOOK NOW</div>
</section>
<h2 class="abs book-title">BOOK NOW, AVOID THE WAIT</h2>

<section class="abs colorful">
  <h2>COLORFUL DRIVE<br>THROUGH CAR CLEAN FACILITY</h2>
  <p>Nam libero tempore, cum soluta nobis est eligendi optio cumque nihil impedit quo minus id quod maxime placeat facere possimus, omnirvo luptas assumenda est, omnis dolor repellendus. Temporibus autemet aut officiis debitis aut rerum necessitatibus saepe eveniet ut et volupt ates repudiandae sint et molestiae.</p>
  <div class="btn-outline">READ MORE</div>
  <div class="photo-circle large" role="img" aria-label="Photo of rainbow-colored car wash brushes over a car"></div>
  <div class="photo-circle small" role="img" aria-label="Photo of a hand washing a car with a sponge"></div>
</section>

<section class="blog">
  <h2 class="abs section-title" style="top:2022px">LATEST BLOG</h2>

  <article class="post" style="left:96px">
    <div class="post-photo"><div class="fill" role="img" aria-label="Photo of a car covered in soap foam" style="background:linear-gradient(160deg,#d9d9d9,#8a8a8a 60%,#4a4a4a)"></div>
      <div class="post-date"><b>01</b><span>NOV</span></div></div>
    <h3>Finibus Bonorum et Malorum</h3>
    <p>Nam libero tempore, cum soluta nobis est eligendi optio cumque nihil impedit quo minus id quod maxim.</p>
    <div class="post-meta"><span><svg width="11" height="11" viewBox="0 0 12 12"><circle cx="6" cy="3.5" r="3" fill="#886aae"/><path d="M0 12c0-3.5 3-5 6-5s6 1.5 6 5z" fill="#886aae"/></svg>Sam Rivera</span><span><svg width="13" height="11" viewBox="0 0 14 12"><path d="M1 1h12v8H6l-3 2.5V9H1z" fill="none" stroke="#886aae" stroke-width="1.5"/></svg>3 Comments</span></div>
  </article>

  <article class="post" style="left:438px">
    <div class="post-photo"><div class="fill" role="img" aria-label="Photo of red and blue car wash brushes over a car" style="background:linear-gradient(180deg,#3f5f95,#d0443c 45%,#2a3550)"></div>
      <div class="post-date"><b>01</b><span>NOV</span></div></div>
    <h3>Finibus Bonorum et Malorum</h3>
    <p>Nam libero tempore, cum soluta nobis est eligendi optio cumque nihil impedit quo minus id quod maxim.</p>
    <div class="post-meta"><span><svg width="11" height="11" viewBox="0 0 12 12"><circle cx="6" cy="3.5" r="3" fill="#886aae"/><path d="M0 12c0-3.5 3-5 6-5s6 1.5 6 5z" fill="#886aae"/></svg>Sam Rivera</span><span><svg width="13" height="11" viewBox="0 0 14 12"><path d="M1 1h12v8H6l-3 2.5V9H1z" fill="none" stroke="#886aae" stroke-width="1.5"/></svg>3 Comments</span></div>
  </article>

  <article class="post" style="left:780px">
    <div class="post-photo"><div class="fill" role="img" aria-label="Photo of a happy driver in a clean car" style="background:linear-gradient(150deg,#a8c48a,#d8d8d2 45%,#7d8a94)"></div>
      <div class="post-date"><b>01</b><span>NOV</span></div></div>
    <h3>Finibus Bonorum et Malorum</h3>
    <p>Nam libero tempore, cum soluta nobis est eligendi optio cumque nihil impedit quo minus id quod maxim.</p>
    <div class="post-meta"><span><svg width="11" height="11" viewBox="0 0 12 12"><circle cx="6" cy="3.5" r="3" fill="#886aae"/><path d="M0 12c0-3.5 3-5 6-5s6 1.5 6 5z" fill="#886aae"/></svg>Sam Rivera</span><span><svg width="13" height="11" viewBox="0 0 14 12"><path d="M1 1h12v8H6l-3 2.5V9H1z" fill="none" stroke="#886aae" stroke-width="1.5"/></svg>3 Comments</span></div>
  </article>
</section>

<footer class="abs footer">
  <svg class="abs" style="left:0;top:0" width="1200" height="80" viewBox="0 0 1200 80">
    <path fill="#1d1d1f" d="M0,80 L0,35 C40,5 90,5 130,40 C170,0 260,0 300,45 C340,20 400,20 440,50 C490,0 600,0 650,45 C690,20 750,20 790,50 C840,5 930,5 970,40 C1010,15 1080,15 1120,45 C1150,25 1190,25 1200,35 L1200,80 Z"/>
    <path fill="none" stroke="#7a58a8" stroke-width="7" d="M0,35 C40,5 90,5 130,40 C170,0 260,0 300,45 C340,20 400,20 440,50 C490,0 600,0 650,45 C690,20 750,20 790,50 C840,5 930,5 970,40 C1010,15 1080,15 1120,45 C1150,25 1190,25 1200,35"/>
  </svg>
  <div class="footer-body"></div>
  <div class="logo"><span class="logo-dot"></span>Foam Harbor</div>

  <div class="foot-col" style="left:436px">
    <h4>INFORMATION</h4>
    <ul class="foot-links"><li>Home</li><li>About</li><li>Services</li><li>Location</li><li>Contact Us</li></ul>
  </div>
  <div class="foot-col" style="left:606px">
    <h4>NEWSLETTER SUBSCRIPTION</h4>
    <p>Register your Email Address to get<br>Information about us</p>
    <div class="news-field">Email Address</div>
    <div class="news-btn">SUBSCRIBE</div>
  </div>
  <div class="foot-col" style="left:910px">
    <h4>CONTACT US</h4>
    <div class="contact-row"><svg width="10" height="14" viewBox="0 0 10 14"><path d="M5 0a5 5 0 0 0-5 5c0 4 5 9 5 9s5-5 5-9a5 5 0 0 0-5-5zm0 7a2 2 0 1 1 0-4 2 2 0 0 1 0 4z" fill="#fff"/></svg><span>Rua das Flores, Lote 12<br>Lagoa Verde - Portugal</span></div>
    <div class="contact-row"><svg width="13" height="13" viewBox="0 0 24 24"><path fill="#fff" d="M6.6 10.8a15 15 0 0 0 6.6 6.6l2.2-2.2c.3-.3.7-.4 1-.2 1.1.4 2.3.6 3.6.6.6 0 1 .4 1 1V20c0 .6-.4 1-1 1A17 17 0 0 1 3 4c0-.6.4-1 1-1h3.5c.6 0 1 .4 1 1 0 1.3.2 2.5.6 3.6.1.3 0 .7-.2 1z"/></svg><span>+1 800 555 0142</span></div>
    <div class="contact-row"><svg width="14" height="11" viewBox="0 0 14 11"><rect width="14" height="11" fill="#fff"/><path d="M0 0l7 6 7-6" fill="none" stroke="#1d1d1f" stroke-width="1.5"/></svg><span>hello@foamharbor.com</span></div>
  </div>

  <div class="foot-rule"></div>
  <div class="copyright">Copyrights © 2018, Foam Harbor. All rights reserved.</div>
  <div class="socials"><span></span><span></span><span></span><span></span><span></span></div>
</footer>

</body>
</html>
```